Rollers & Glides.com

Vertical Business Card with focus on branding with our icon. Information on card will be logo, persons name, position, phone number, email address and website. Use the the name Marcus Delby, position President, phone number 480.315.7792, email Marcus@rollersandglides-example.com, website www.rollersandglides-example.com.

```html
<!DOCTYPE html>
<html lang="en">
<head>
<meta charset="utf-8">
<title>Rollers &amp; Glides.com — Business Card</title>
<link rel="stylesheet" href="https://fonts.googleapis.com/css2?family=Roboto+Condensed:wght@400&family=Roboto:wght@400;700&family=Arimo:wght@400&display=swap">
<style>
  :root {
    --stage: #222120;
    --brand-blue: #3461ab;
    --brand-tint: #e8edf4;
    --paper: #ffffff;
    --ink: #222222;
  }
  * { margin: 0; padding: 0; box-sizing: border-box; }
  html, body {
    width: 1065px;
    height: 1200px;
    overflow: hidden;
    background: var(--stage);
  }
  .stage { position: relative; width: 1065px; height: 1200px; }

  .card {
    position: absolute;
    width: 582px;
    height: 362px;
    overflow: hidden;
  }

  /* Front */
  .card--front {
    left: 292px;
    top: 218px;
    background: var(--paper);
    border-radius: 0 175px 175px 0 / 0 181px 181px 0;
  }
  .front__backdrop-circle {
    position: absolute;
    left: 362px;
    top: 60px;
    width: 240px;
    height: 240px;
    border-radius: 50%;
    background: var(--brand-tint);
  }
  .brand {
    position: absolute;
    display: flex;
    align-items: center;
    gap: 12px;
    font-family: "Roboto Condensed", "Arial Narrow", sans-serif;
    font-weight: 400;
    letter-spacing: 0.5px;
    white-space: nowrap;
  }
  .brand__dot {
    border-radius: 50%;
    flex: none;
  }
  .card--front .brand {
    left: 48px;
    top: 72px;
    font-size: 34px;
    color: var(--brand-blue);
  }
  .card--front .brand__dot {
    width: 34px;
    height: 34px;
    background: var(--brand-blue);
  }

  .person {
    position: absolute;
    left: 124px;
    top: 172px;
    font-family: "Roboto", Arial, sans-serif;
  }
  .person__name {
    font-size: 22px;
    font-weight: 700;
    color: var(--brand-blue);
    line-height: 1;
  }
  .person__role {
    margin-top: 5px;
    font-size: 17px;
    color: var(--ink);
    line-height: 1;
  }

  .contact {
    position: absolute;
    left: 122px;
    top: 240px;
    list-style: none;
    font-family: "Arimo", Arial, sans-serif;
    font-size: 17px;
    color: var(--ink);
  }
  .contact__item {
    display: flex;
    align-items: center;
    gap: 7px;
    height: 21.5px;
    white-space: nowrap;
  }
  .contact__icon {
    width: 15px;
    height: 15px;
    flex: none;
    fill: var(--brand-blue);
  }
  .contact__domain { color: var(--brand-blue); }

  /* Back */
  .card--back {
    left: 263px;
    top: 623px;
    background: var(--brand-blue);
    border-radius: 175px 0 0 175px / 181px 0 0 181px;
  }
  .card--back .brand {
    left: 0;
    right: 0;
    top: 78px;
    flex-direction: column;
    gap: 26px;
    font-size: 37px;
    color: var(--paper);
  }
  .card--back .brand__dot {
    width: 80px;
    height: 80px;
    background: var(--paper);
    margin-left: -10px;
  }
</style>
</head>
<body>
<main class="stage">

  <section class="card card--front" aria-label="Business card front">
    <div class="front__backdrop-circle" aria-hidden="true"></div>

    <div class="brand">
      <span class="brand__dot" aria-hidden="true"></span>
      <span class="brand__name">Rollers &amp; Glides.com</span>
    </div>

    <div class="person">
      <p class="person__name">MARCUS DELBY</p>
      <p class="person__role">President</p>
    </div>

    <ul class="contact">
      <li class="contact__item">
        <svg class="contact__icon" viewBox="0 0 24 24" aria-hidden="true">
          <path d="M6.6 10.8c1.4 2.8 3.8 5.1 6.6 6.6l2.2-2.2c.3-.3.7-.4 1-.2 1.1.4 2.3.6 3.6.6.6 0 1 .4 1 1V20c0 .6-.4 1-1 1C10.6 21 3 13.4 3 4c0-.6.4-1 1-1h3.5c.6 0 1 .4 1 1 0 1.3.2 2.5.6 3.6.1.3 0 .7-.2 1L6.6 10.8z"/>
          <path d="M14 3.5a7 7 0 0 1 6.5 6.5h-1.8A5.2 5.2 0 0 0 14 5.3zM14 7a3.5 3.5 0 0 1 3 3h-1.8A1.8 1.8 0 0 0 14 8.8z"/>
        </svg>
        <span>480.315.7792</span>
      </li>
      <li class="contact__item">
        <svg class="contact__icon" viewBox="0 0 24 24" aria-hidden="true">
          <path d="M2 5h20v14H2zM3.5 6.5v.6L12 13l8.5-5.9v-.6zM3.5 17.5l6-5.2-6-4.2zm17 0v-9.4l-6 4.2z"/>
        </svg>
        <span>Marcus@rollersandglides-example.com</span>
      </li>
      <li class="contact__item">
        <svg class="contact__icon" viewBox="0 0 24 24" aria-hidden="true">
          <path d="M12 2a10 10 0 1 0 0 20 10 10 0 0 0 0-20zm0 1.8c.9 0 2 1.6 2.5 4.2h-5C10 5.4 11.1 3.8 12 3.8zM9.2 4.3A12 12 0 0 0 7.7 8H4.9a8.2 8.2 0 0 1 4.3-3.7zm5.6 0A8.2 8.2 0 0 1 19.1 8h-2.8a12 12 0 0 0-1.5-3.7zM4.2 9.8h3.2a17 17 0 0 0 0 4.4H4.2a8.2 8.2 0 0 1 0-4.4zm5 0h5.6a15 15 0 0 1 0 4.4H9.2a15 15 0 0 1 0-4.4zm7.4 0h3.2a8.2 8.2 0 0 1 0 4.4h-3.2a17 17 0 0 0 0-4.4zM4.9 16h2.8a12 12 0 0 0 1.5 3.7A8.2 8.2 0 0 1 4.9 16zm4.6 0h5c-.5 2.6-1.6 4.2-2.5 4.2S10 18.6 9.5 16zm6.8 0h2.8a8.2 8.2 0 0 1-4.3 3.7 12 12 0 0 0 1.5-3.7z"/>
        </svg>
        <span>www.<span class="contact__domain">rollersandglides-example</span>.com</span>
      </li>
    </ul>
  </section>

  <section class="card card--back" aria-label="Business card back">
    <div class="brand">
      <span class="brand__dot" aria-hidden="true"></span>
      <span class="brand__name">Rollers &amp; Glides.com</span>
    </div>
  </section>

</main>
</body>
</html>
```